Doctor Formulated Medical Cosmetics

Halvessa Rue is an E-commerce site for high end Medical Cosmetics designed to treat specific skin problems. The Halvessa Rue difference/advantage is that all creams and serums are:
Doctor Formulated, Freshly Handmade, Registered Pharmacy.
The Site also provides real doctor Dermatology Consultations, Library (with a list of - 1. Active Ingredients in the creams with description of their effects, 2. Skin Conditions with information on what causes the condition and typical treatment approaches and outcomes. 3. Resources from Dermatology Journals and literature on the conditions.)
Header Information: Halvessa Rue, languages EN, BG, Register / log in, Shopping Bag. This field should be narrow.
Categories (horizontal): Home, Face, Body, Hair Care, Skin Conditions, Doctor Consultation, Library
The Landing Page should have only one well organized picture, which is intended to create the feeling of luxury, freedom and relaxation. It will be large and will fill the whole screen. All text should be on transparent or similar color fields. Please use the color of the text to create also the feeling of conservative luxury.
Written message / image overlay Halvessa Rue(logo), Skin Care, Doctor Formulated, Freshly Handmade, Registered Pharmacy.
Please study the Landing Page of this site as an example: www.marivelta.com
Under the Landing Page, there should be a slider with 4 of our products.
Underneath: Four Blog Articles (large pictures for maximum impact and luxury text underneath).
Underneath: Banner for Dermatologist Consultation, (button for Start Your Case Now).
Underneath: Two pictures in a line - Library (with books), and Active Ingredients.
Footer: Philosophy, Categories, Customer Care
Please adhere to the color palate provided in the pictures (as attachments). Provided are some examples of Web Sites with the desired look and feel. www.quillon.com , www.tavishrowe.com .
Please use different shades of gray, white, beige and gold colors, and black. Our products will be in brown glass jars and bottles to convey the professional, pharmacy made nature of the creams and lotions.
We find the following Front Page very attractive and effective - www.marivelta.com , with its full page image and overlaying text.
Please have a look at this link for the Landing page.
http://www.framstockly.com/detail/video/woman-lying-on-a-black-sand-beach-in-a-bikini-stock-footage/31862074
I would like to use it in the animated version to achieve the WOW effect. I have uploaded the jpeg version for it, so you will be able create your design.
For the Landing page design, please use only the two uploaded pictures of a woman laying at the beach. Let's see how each of them will look like.
Thank you for your help.

```html
<!DOCTYPE html>
<html lang="en">
<head>
<meta charset="utf-8">
<title>Halvessa Rue — Doctor Formulated Medical Cosmetics</title>
<link href="https://fonts.googleapis.com/css2?family=Marcellus&family=Open+Sans:wght@400;600;700&display=swap" rel="stylesheet">
<style>
:root{
  --black:#0b0b0b;
  --ink:#333333;
  --muted:#666666;
  --gold:#c9a55a;
  --gold-light:#d8b878;
  --line:#e4e4e4;
  --card:#f7f7f7;
  --white:#ffffff;
  --footer:#161616;
  --hero-a:#e9ecef;
  --hero-b:#c7ccd3;
}
*{margin:0;padding:0;box-sizing:border-box}
html,body{width:1200px;height:2871px;overflow:hidden}
body{font-family:'Open Sans',Arial,sans-serif;color:var(--ink);background:var(--white);position:relative}
.serif{font-family:'Marcellus',Georgia,serif}
a{color:inherit;text-decoration:none}

/* Header */
.site-header{position:absolute;left:0;top:0;width:1200px;height:134px;background:var(--black)}
.brand{position:absolute;left:100px;top:42px;display:flex;align-items:center;gap:12px;font-family:'Marcellus',Georgia,serif;font-size:36px;color:var(--gold)}
.brand-dot{width:40px;height:40px;border:2px solid var(--gold);border-radius:50%}
.cart{position:absolute;left:476px;top:50px;display:flex;align-items:center;gap:10px;color:var(--white)}
.cart-icon{width:34px;height:34px;border:1px solid #777;border-radius:50%;display:flex;align-items:center;justify-content:center}
.cart-text b{display:block;font-size:13px;font-weight:600}
.cart-text span{font-size:10px;color:#bbb}
.pharmacy-link{position:absolute;left:640px;top:60px;font-size:12px;font-weight:700;color:var(--white)}
.lang{position:absolute;left:804px;top:51px;width:104px;height:30px;border:1px solid #888;color:var(--white);font-size:10px;display:flex;align-items:center;justify-content:center;gap:6px}
.lang-flag{width:16px;height:10px;background:#3a4f8c}
.btn-register{position:absolute;left:920px;top:51px;width:86px;height:30px;background:var(--gold);color:var(--white);font-size:12px;display:flex;align-items:center;justify-content:center}
.btn-login{position:absolute;left:1020px;top:51px;width:80px;height:30px;border:1px solid var(--white);color:var(--white);font-size:12px;font-weight:600;display:flex;align-items:center;justify-content:center}

/* Navigation */
.main-nav{position:absolute;left:0;top:134px;width:1200px;height:52px;background:linear-gradient(var(--gold-light),var(--gold))}
.main-nav ul{list-style:none;display:flex;margin-left:100px;height:52px}
.main-nav li{display:flex;align-items:center;padding:0 28px;font-family:'Marcellus',Georgia,serif;font-size:17px;color:var(--white);border-right:1px solid rgba(255,255,255,.25)}
.main-nav li.active{background:#2a2a2a;padding:0 24px}

/* Hero */
.hero{position:absolute;left:0;top:186px;width:1200px;height:516px;background:linear-gradient(90deg,var(--hero-a),#dfe3e8 55%,var(--hero-b))}
.hero-photo{position:absolute;left:610px;top:0;width:590px;height:516px;background:radial-gradient(ellipse at 60% 40%,#e8c2aa 0%,#d6a98e 30%,rgba(199,204,211,0) 70%)}
.hero-brand{position:absolute;left:127px;top:100px;display:flex;align-items:center;gap:12px;font-family:'Marcellus',Georgia,serif;font-size:38px;color:#333}
.hero-brand .brand-dot{border-color:#333;width:44px;height:44px}
.hero-points{position:absolute;left:127px;top:186px;list-style:none}
.hero-points li{font-family:'Marcellus',Georgia,serif;font-size:17px;color:#333;height:31px;display:flex;align-items:center;gap:10px}
.hero-points svg{flex:none}
.btn-gold{display:inline-flex;align-items:center;gap:8px;background:var(--gold);color:var(--white);font-size:12px;font-weight:600;padding:0 16px;height:34px}
.hero .btn-gold{position:absolute;left:127px;top:323px}
.dots{position:absolute;left:127px;top:390px;display:flex;gap:6px}
.dots span{width:12px;height:12px;border-radius:50%;background:var(--white)}
.dots span.on{background:#222}

/* Section headings */
.section-title{position:absolute;left:100px;display:flex;align-items:center;gap:14px;font-family:'Marcellus',Georgia,serif;font-size:25px;color:#222}
.title-mark{width:46px;height:46px;border:2px solid var(--gold);border-radius:50%}
.arrows{position:absolute;left:1050px;display:flex;gap:4px}
.arrows span{width:24px;height:24px;border:1px solid #999;border-radius:50%;display:flex;align-items:center;justify-content:center}

/* Products */
.product{position:absolute;top:820px;width:233px;height:287px;border:1px solid var(--line);background:var(--white)}
.product-photo{height:207px;background:linear-gradient(#ffffff,#ececec);border-bottom:1px solid var(--line)}
.product-cart{position:absolute;right:16px;top:16px;width:26px;height:26px;border-radius:50%;background:var(--gold);display:flex;align-items:center;justify-content:center}
.product-name{position:absolute;left:14px;top:223px;font-family:'Marcellus',Georgia,serif;font-size:16px;color:#333}
.price{position:absolute;right:12px;top:223px;font-size:16px;color:var(--gold)}
.price-old{position:absolute;right:14px;top:250px;font-size:12px;color:#999;text-decoration:line-through}
.stars{position:absolute;left:14px;top:254px;font-size:11px;letter-spacing:1px;color:var(--gold)}
.stars i{font-style:normal;color:#ccc}

/* Blog */
.blog-card{position:absolute;width:486px;height:172px;background:var(--card);border:1px solid var(--line)}
.blog-photo{position:absolute;left:0;top:0;width:190px;height:170px}
.blog-body{position:absolute;left:212px;top:16px;width:256px}
.blog-body h3{font-family:'Marcellus',Georgia,serif;font-weight:400;font-size:16px;color:#333}
.blog-body time{display:block;margin:12px 0 10px;font-size:11px;color:#333;font-family:'Marcellus',Georgia,serif}
.blog-body p{font-size:11px;line-height:19px;color:#555}

/* Consultation banner */
.consult{position:absolute;left:0;top:1667px;width:1200px;height:433px;background:linear-gradient(90deg,#8a6a5a 0%,#5a4038 35%,#2a1b19 60%,#1e1414 100%)}
.consult-photo{position:absolute;left:0;top:0;width:640px;height:433px;background:radial-gradient(ellipse at 45% 45%,#d9ab8f 0%,#b98a72 30%,rgba(42,27,25,0) 72%)}
.consult h2{position:absolute;left:731px;top:95px;font-family:'Marcellus',Georgia,serif;font-weight:400;font-size:42px;line-height:42px;color:var(--white)}
.consult p{position:absolute;left:735px;top:205px;width:360px;font-size:14px;line-height:26px;color:var(--white)}
.consult .btn-gold{position:absolute;left:735px;top:280px}

/* News */
.news{position:absolute;top:2214px;width:311px}
.news-photo{height:152px}
.news h3{margin-top:14px;font-size:14px;font-weight:400;color:#333}
.news .meta{margin-top:10px;font-size:11px;color:#555;display:flex;align-items:center;gap:5px}
.news p{margin-top:8px;font-size:11px;line-height:20px;color:#555;padding-bottom:14px;border-bottom:1px solid var(--line)}

/* Footer */
.site-footer{position:absolute;left:0;top:2544px;width:1200px;height:266px;background:var(--footer)}
.footer-about{position:absolute;left:0;top:0;width:383px;height:266px;background:linear-gradient(90deg,#2a1e18,#3a2a22 55%,#1c1612)}
.footer-about .brand{left:100px;top:50px;font-size:32px}
.footer-about .brand-dot{width:36px;height:36px}
.footer-about p{position:absolute;left:100px;top:128px;width:255px;font-size:11px;line-height:19px;color:var(--white)}
.footer-col{position:absolute;top:48px}
.footer-col h4{font-family:'Marcellus',Georgia,serif;font-weight:400;font-size:16px;color:var(--white);margin-bottom:18px}
.footer-col li{list-style:none;font-size:12px;color:#ddd;height:26px}
.contact-row{display:flex;gap:10px;font-size:12px;color:#ddd;margin-bottom:14px;line-height:18px}
.social{display:flex;gap:8px;margin-top:6px}
.social span{width:24px;height:24px;border:1px solid #bbb;border-radius:50%}
.bottom-bar{position:absolute;left:0;top:2810px;width:1200px;height:61px;background:var(--gold)}
.bottom-bar small{position:absolute;left:100px;top:22px;font-size:11px;color:var(--white)}
.cards{position:absolute;left:922px;top:15px;display:flex;gap:8px}
.cards span{width:38px;height:26px;background:var(--white);border-radius:3px}
.page-no{position:absolute;left:1153px;top:38px;font-size:10px;color:var(--white)}
</style>
</head>
<body>

<header class="site-header">
  <div class="brand"><span class="brand-dot"></span>Halvessa Rue</div>
  <div class="cart">
    <span class="cart-icon"><svg width="14" height="12" viewBox="0 0 14 12"><path d="M0 1h2.5l2 7h7l1.5-5H4" fill="none" stroke="#fff" stroke-width="1.4"/><circle cx="5.5" cy="10.5" r="1" fill="#fff"/><circle cx="10.5" cy="10.5" r="1" fill="#fff"/></svg></span>
    <div class="cart-text"><b>MY CART</b><span>0 ITEM(S) - $0.00</span></div>
  </div>
  <a class="pharmacy-link">DOCTOR &nbsp;/&nbsp; PHARMACY</a>
  <div class="lang"><span class="lang-flag"></span>ENGLISH <svg width="8" height="5" viewBox="0 0 8 5"><path d="M0 0l4 5 4-5z" fill="#fff"/></svg></div>
  <a class="btn-register">REGISTER</a>
  <a class="btn-login">LOG IN</a>
</header>

<nav class="main-nav">
  <ul>
    <li class="active">Home</li><li>Face</li><li>Body</li><li>Hair Care</li><li>Skin Concerns</li><li>Dermatologist Consultation</li><li>Library</li>
  </ul>
</nav>

<section class="hero">
  <div class="hero-photo" role="img" aria-label="Portrait of a woman with glowing skin against a soft grey background"></div>
  <div class="hero-brand"><span class="brand-dot"></span>Halvessa Rue</div>
  <ul class="hero-points">
    <li><svg width="12" height="12" viewBox="0 0 12 12"><circle cx="6" cy="6" r="6" fill="#333"/><path d="M5 3.5 7.5 6 5 8.5" stroke="#fff" stroke-width="1.4" fill="none"/></svg>Doctor Formulated</li>
    <li><svg width="12" height="12" viewBox="0 0 12 12"><circle cx="6" cy="6" r="6" fill="#333"/><path d="M5 3.5 7.5 6 5 8.5" stroke="#fff" stroke-width="1.4" fill="none"/></svg>Freshly Handmade</li>
    <li><svg width="12" height="12" viewBox="0 0 12 12"><circle cx="6" cy="6" r="6" fill="#333"/><path d="M5 3.5 7.5 6 5 8.5" stroke="#fff" stroke-width="1.4" fill="none"/></svg>Registered Pharmacy</li>
    <li><svg width="12" height="12" viewBox="0 0 12 12"><circle cx="6" cy="6" r="6" fill="#333"/><path d="M5 3.5 7.5 6 5 8.5" stroke="#fff" stroke-width="1.4" fill="none"/></svg>Highest Ethical Standards</li>
  </ul>
  <a class="btn-gold">SHOP NOW <svg width="12" height="12" viewBox="0 0 12 12"><circle cx="6" cy="6" r="6" fill="#fff"/><path d="M5 3.5 7.5 6 5 8.5" stroke="#c9a55a" stroke-width="1.4" fill="none"/></svg></a>
  <div class="dots"><span class="on"></span><span></span><span></span><span></span></div>
</section>

<h2 class="section-title" style="top:745px"><span class="title-mark"></span>OUR PRODUCTS</h2>
<div class="arrows" style="top:754px"><span><svg width="8" height="8" viewBox="0 0 8 8"><path d="M5.5 1 2.5 4l3 3" stroke="#777" fill="none"/></svg></span><span><svg width="8" height="8" viewBox="0 0 8 8"><path d="M2.5 1l3 3-3 3" stroke="#777" fill="none"/></svg></span></div>

<div class="product" style="left:100px"><div class="product-photo" role="img" aria-label="Cream jar and tube with pink flowers"></div><span class="product-cart"><svg width="12" height="10" viewBox="0 0 14 12"><path d="M0 1h2.5l2 7h7l1.5-5H4" fill="none" stroke="#fff" stroke-width="1.6"/></svg></span><span class="product-name">Sed ut perspiciatis</span><span class="price">£20.00</span><span class="stars">★★★<i>☆☆</i></span><span class="price-old">£30.00</span></div>
<div class="product" style="left:356px"><div class="product-photo" role="img" aria-label="Lotion tube with pump"></div><span class="product-cart"><svg width="12" height="10" viewBox="0 0 14 12"><path d="M0 1h2.5l2 7h7l1.5-5H4" fill="none" stroke="#fff" stroke-width="1.6"/></svg></span><span class="product-name">Sed ut perspiciatis</span><span class="price">£20.00</span><span class="stars">★★★<i>☆☆</i></span><span class="price-old">£30.00</span></div>
<div class="product" style="left:613px"><div class="product-photo" role="img" aria-label="Set of white skincare bottles and jars"></div><span class="product-cart"><svg width="12" height="10" viewBox="0 0 14 12"><path d="M0 1h2.5l2 7h7l1.5-5H4" fill="none" stroke="#fff" stroke-width="1.6"/></svg></span><span class="product-name">Sed ut perspiciatis</span><span class="price">£20.00</span><span class="stars">★★★<i>☆☆</i></span><span class="price-old">£30.00</span></div>
<div class="product" style="left:866px"><div class="product-photo" role="img" aria-label="Serum dropper bottle"></div><span class="product-cart"><svg width="12" height="10" viewBox="0 0 14 12"><path d="M0 1h2.5l2 7h7l1.5-5H4" fill="none" stroke="#fff" stroke-width="1.6"/></svg></span><span class="product-name">Sed ut perspiciatis</span><span class="price">£20.00</span><span class="stars">★★★<i>☆☆</i></span><span class="price-old">£30.00</span></div>

<h2 class="section-title" style="top:1158px"><span class="title-mark"></span>BLOG ARTICLES</h2>
<div class="arrows" style="top:1165px"><span><svg width="8" height="8" viewBox="0 0 8 8"><path d="M5.5 1 2.5 4l3 3" stroke="#777" fill="none"/></svg></span><span><svg width="8" height="8" viewBox="0 0 8 8"><path d="M2.5 1l3 3-3 3" stroke="#777" fill="none"/></svg></span></div>

<article class="blog-card" style="left:100px;top:1231px"><div class="blog-photo" role="img" aria-label="Woman with curly hair in warm light" style="background:linear-gradient(135deg,#6b3f2a,#c48a5e)"></div><div class="blog-body"><h3>Nulla at diam ornare, aliquam</h3><time>MAY 25, 2016</time><p>Nulla at diam ornare, aliquam urna vel, commod urna. Nam id risus a est luctus consectetur quis eget libero. Suspendisse potenti. Pellentesque habitant morbi tristique senectus</p></div></article>
<article class="blog-card" style="left:614px;top:1231px"><div class="blog-photo" role="img" aria-label="Pharmacist standing in a store" style="background:linear-gradient(135deg,#8a6a4a,#d9c3a8)"></div><div class="blog-body"><h3>Nulla at diam ornare, aliquam</h3><time>MAY 25, 2016</time><p>Nulla at diam ornare, aliquam urna vel, commod urna. Nam id risus a est luctus consectetur quis eget libero. Suspendisse potenti. Pellentesque habitant morbi tristique senectus</p></div></article>
<article class="blog-card" style="left:100px;top:1430px"><div class="blog-photo" role="img" aria-label="Woman walking through a bright airport" style="background:linear-gradient(135deg,#c9b48e,#7a8a96)"></div><div class="blog-body"><h3>Nulla at diam ornare, aliquam</h3><time>MAY 25, 2016</time><p>Nulla at diam ornare, aliquam urna vel, commod urna. Nam id risus a est luctus consectetur quis eget libero. Suspendisse potenti. Pellentesque habitant morbi tristique senectus</p></div></article>
<article class="blog-card" style="left:614px;top:1430px"><div class="blog-photo" role="img" aria-label="Red lips and manicured nails close-up" style="background:linear-gradient(135deg,#3a1e18,#c8324a)"></div><div class="blog-body"><h3>Nulla at diam ornare, aliquam</h3><time>MAY 25, 2016</time><p>Nulla at diam ornare, aliquam urna vel, commod urna. Nam id risus a est luctus consectetur quis eget libero. Suspendisse potenti. Pellentesque habitant morbi tristique senectus</p></div></article>

<section class="consult">
  <div class="consult-photo" role="img" aria-label="Doctor marking a patient's face before a dermatology consultation"></div>
  <h2>the Dermatologist<br>Consultation</h2>
  <p>Sed ut perspiciatis unde omnis iste natus error sit voluptatem accusantium doloremque</p>
  <a class="btn-gold">READ MORE <svg width="12" height="12" viewBox="0 0 12 12"><circle cx="6" cy="6" r="6" fill="#fff"/><path d="M5 3.5 7.5 6 5 8.5" stroke="#c9a55a" stroke-width="1.4" fill="none"/></svg></a>
</section>

<h2 class="section-title" style="top:2137px"><span class="title-mark"></span>LATEST NEWS</h2>
<div class="arrows" style="top:2151px"><span><svg width="8" height="8" viewBox="0 0 8 8"><path d="M5.5 1 2.5 4l3 3" stroke="#777" fill="none"/></svg></span><span><svg width="8" height="8" viewBox="0 0 8 8"><path d="M2.5 1l3 3-3 3" stroke="#777" fill="none"/></svg></span></div>

<article class="news" style="left:100px"><div class="news-photo" role="img" aria-label="Woman with wavy auburn hair" style="background:linear-gradient(135deg,#3a1a10,#b0562e)"></div><h3>Nemo enim ipsam voluptatem</h3><div class="meta"><svg width="10" height="10" viewBox="0 0 10 10"><circle cx="5" cy="5" r="4.3" fill="none" stroke="#555"/><path d="M5 2.5V5h2" stroke="#555" fill="none"/></svg>3 minutes ago, 0 comments</div><p>Lorem ipsum dolor sit amet, consectetur adipiscing elit, sed do eiusmod tempor ncididunt ut labore et dolore</p></article>
<article class="news" style="left:450px"><div class="news-photo" role="img" aria-label="Woman at a mirror in a dressing room" style="background:linear-gradient(135deg,#d6d3d0,#6a5a52)"></div><h3>Nemo enim ipsam voluptatem</h3><div class="meta"><svg width="10" height="10" viewBox="0 0 10 10"><circle cx="5" cy="5" r="4.3" fill="none" stroke="#555"/><path d="M5 2.5V5h2" stroke="#555" fill="none"/></svg>3 minutes ago, 0 comments</div><p>Lorem ipsum dolor sit amet, consectetur adipiscing elit, sed do eiusmod tempor ncididunt ut labore et dolore</p></article>
<article class="news" style="left:792px;width:308px"><div class="news-photo" role="img" aria-label="Smiling woman with curly hair on a red background" style="background:linear-gradient(135deg,#5a2a1e,#c8203a)"></div><h3>Nemo enim ipsam voluptatem</h3><div class="meta"><svg width="10" height="10" viewBox="0 0 10 10"><circle cx="5" cy="5" r="4.3" fill="none" stroke="#555"/><path d="M5 2.5V5h2" stroke="#555" fill="none"/></svg>3 minutes ago, 0 comments</div><p>Lorem ipsum dolor sit amet, consectetur adipiscing elit, sed do eiusmod tempor ncididunt ut labore et dolore</p></article>

<footer class="site-footer">
  <div class="footer-about" role="img" aria-label="Dim portrait of a woman behind the footer text">
    <div class="brand"><span class="brand-dot"></span>Halvessa Rue</div>
    <p>Lorem ipsum dolor sit amet conse ctetur adipisicing elit, sed do eiusmod tempor incididunt ut labore et dolore magna aliqua. Ut enim ad minim veniam, quis nostrud exercitation. Lorem ipsum dolor sit amet conse ctetur</p>
  </div>
  <div class="footer-col" style="left:438px"><h4>WHY BUY FROM US</h4><ul><li>Face</li><li>Body</li><li>Hair Care</li><li>Skin Concerns</li><li>Dermatologist Consultation</li><li>Library</li></ul></div>
  <div class="footer-col" style="left:678px"><h4>MY ACCOUNT</h4><ul><li>My orders</li><li>My credit slips</li><li>My addresses</li><li>My personal info</li><li>Terms and conditions</li><li>Privacy Policy</li></ul></div>
  <div class="footer-col" style="left:903px"><h4>CONTACTS</h4>
    <div class="contact-row"><svg width="12" height="16" viewBox="0 0 12 16"><path d="M6 1a5 5 0 0 0-5 5c0 4 5 9 5 9s5-5 5-9a5 5 0 0 0-5-5z" fill="none" stroke="#ccc"/><circle cx="6" cy="6" r="1.8" fill="#ccc"/></svg><span>PO BOX 412, 18 Larch Street,<br>Tamberly, NSW 2690</span></div>
    <div class="contact-row"><svg width="12" height="12" viewBox="0 0 12 12"><path d="M2 1l2 0 1 3-1.5 1a7 7 0 0 0 3.5 3.5L8 7l3 1v2a1 1 0 0 1-1 1A9 9 0 0 1 1 2a1 1 0 0 1 1-1z" fill="#ccc"/></svg><span>Call Us: 1800 555 019</span></div>
    <div class="contact-row"><svg width="12" height="10" viewBox="0 0 12 10"><rect x=".5" y=".5" width="11" height="9" fill="none" stroke="#ccc"/><path d="M.5 .5 6 5l5.5-4.5" fill="none" stroke="#ccc"/></svg><span>info@halvessarue.com</span></div>
    <div class="social"><span></span><span></span><span></span><span></span></div>
  </div>
</footer>

<div class="bottom-bar">
  <small>Copyright © 2016 Halvessa Rue. All rights reserved</small>
  <div class="cards"><span></span><span></span><span></span><span></span></div>
  <span class="page-no">07</span>
</div>

</body>
</html>
```